I need a Floral Supermarket Planogram to show suggested flower Displays

Hello,
We are a flower company that distributes fresh cut flowers to mass market customers. We want to be able to present a FLoral planogram to buyers that could showcase some different products and how they could display them in their store. Ive attached pictures of what a basic planogram looks like. I want a graphic design template where i can insert different pictures with the flower name and item number. The flower pictures would be circular like a headshot. You can see examples of the flowers we sell at www.brindlemeadowgoods.com
Im also uploading pictures of what the actual displays look like in the stores. I would like for the graphic design to mirror that and look kind of realistic.

Its important that I can adjust the items by myself as a PDF document in the end product. We change items seasonally and as the buyers request.

Thank you,

Colors
0054AA
0677BA
7BADD7
CADEEF
E8F1F8
0094D4
00A9DD
6FCCEA
C7EBF8
E9F6FB
59FF00
82FF00
B8FF75
E3FFCB
F4FFEA

Requirements
Must have
• be able to adjust the product pictures and names by myself at the end

```html
<!DOCTYPE html>
<html lang="en">
<head>
<meta charset="utf-8">
<title>Brindle Meadow – Floral Planogram</title>
<link href="https://fonts.googleapis.com/css2?family=Open+Sans:wght@600;700;800&display=swap" rel="stylesheet">
<style>
  :root {
    --paper: #fbfbfa;
    --navy: #2e3192;
    --leaf: #8dc63f;
    --leaf-dark: #6fa22c;
    --board: #d2ad84;
    --board-edge: #b08863;
    --board-light: #e2c3a0;
    --post: #7b5433;
    --post-light: #9a6c45;
    --ring: #c9c9c9;
  }
  * { box-sizing: border-box; margin: 0; padding: 0; }
  html, body { width: 991px; height: 1200px; overflow: hidden; }
  body {
    background: var(--paper);
    font-family: "Open Sans", Arial, sans-serif;
    position: relative;
  }

  .brand {
    position: absolute; top: 62px; left: 0; width: 991px;
    display: flex; justify-content: center; align-items: center; gap: 18px;
  }
  .brand-dot { width: 64px; height: 64px; border-radius: 50%; background: var(--leaf); }
  .brand-name {
    color: var(--navy); font-weight: 800; font-size: 38px; line-height: 1.02;
    letter-spacing: 0.5px; text-transform: uppercase;
  }

  .rack-post {
    position: absolute; top: 372px; width: 26px; height: 760px; border-radius: 4px;
    background: linear-gradient(90deg, var(--post-light), var(--post) 55%, #6a4629);
    box-shadow: 2px 2px 4px rgba(0,0,0,.25);
  }
  .rack-post.left { left: 52px; }
  .rack-post.right { left: 912px; }

  .shelf {
    position: absolute; left: 64px; width: 862px; height: 122px;
  }
  .shelf-board {
    position: absolute; left: 0; right: 0; top: 96px; height: 22px;
    background: linear-gradient(180deg, var(--board-light) 0 35%, var(--board) 35% 75%, var(--board-edge) 75%);
  }

  .product {
    position: absolute; top: 0; width: 190px; text-align: center;
  }
  .product-photo {
    width: 150px; height: 150px; margin: -75px auto 0; border-radius: 50%;
    border: 2px solid var(--ring);
  }
  .product-label {
    position: absolute; left: 20px; top: 90px; width: 150px; height: 32px;
    background: var(--leaf); color: #fff; font-weight: 700; font-size: 13.5px;
    display: flex; align-items: center; justify-content: center;
    box-shadow: 0 3px 0 var(--leaf-dark), 0 5px 6px rgba(0,0,0,.18);
  }

  .site {
    position: absolute; top: 1146px; left: 0; width: 991px; text-align: center;
    color: var(--navy); font-weight: 700; font-size: 20px;
  }
</style>
</head>
<body>
  <header class="brand">
    <span class="brand-dot"></span>
    <span class="brand-name">Brindle<br>Meadow</span>
  </header>

  <div class="rack-post left"></div>
  <div class="rack-post right"></div>

  <section class="shelf" style="top:310px">
    <div class="shelf-board"></div>
    <div class="product" style="left:45px"><div class="product-photo" role="img" aria-label="Yellow alstroemeria blooms" style="background:radial-gradient(circle at 40% 40%,#f8e060,#e8b81e 70%,#7a9a3a)"></div><div class="product-label">Alstroemeria Yellow</div></div>
    <div class="product" style="left:235px"><div class="product-photo" role="img" aria-label="White spring aster flowers" style="background:radial-gradient(circle,#d8d08a 8%,#f3f3ee 25%,#d6d8d2 70%,#8a9a7a)"></div><div class="product-label">Aster Spring White</div></div>
    <div class="product" style="left:424px"><div class="product-photo" role="img" aria-label="Purple spring aster flowers" style="background:radial-gradient(circle,#e8d060 10%,#a68ae0 30%,#7e5fc4 75%,#5a7a3a)"></div><div class="product-label">Aster Spring Purple</div></div>
    <div class="product" style="left:614px"><div class="product-photo" role="img" aria-label="White baby's breath sprays" style="background:radial-gradient(circle,#f4f5f7,#d6d9de 70%,#a8adb4)"></div><div class="product-label">Baby's breath</div></div>
  </section>

  <section class="shelf" style="top:529px">
    <div class="shelf-board"></div>
    <div class="product" style="left:45px"><div class="product-photo" role="img" aria-label="Green bells of Ireland stems" style="background:radial-gradient(circle,#f2f5ea,#9cc460 55%,#5e8a2a)"></div><div class="product-label">Bells of Ireland</div></div>
    <div class="product" style="left:235px"><div class="product-photo" role="img" aria-label="Bird of paradise flower" style="background:radial-gradient(circle at 50% 40%,#f08a3a,#eab08c 45%,#d9a688 80%)"></div><div class="product-label">Bird of Paradise</div></div>
    <div class="product" style="left:424px"><div class="product-photo" role="img" aria-label="Blue-grey eryngium thistles" style="background:radial-gradient(circle,#8a94a0,#4e5662 65%,#2e343c)"></div><div class="product-label">Erygngium</div></div>
    <div class="product" style="left:614px"><div class="product-photo" role="img" aria-label="Orange gerbera daisy" style="background:radial-gradient(circle,#8a4a10 10%,#f6b62a 30%,#f7a51b 80%)"></div><div class="product-label">Gerberas</div></div>
  </section>

  <section class="shelf" style="top:749px">
    <div class="shelf-board"></div>
    <div class="product" style="left:45px"><div class="product-photo" role="img" aria-label="White hydrangea heads" style="background:radial-gradient(circle,#f4f6ee,#dfe6d2 60%,#8a9a86)"></div><div class="product-label">Hydrangeas</div></div>
    <div class="product" style="left:235px"><div class="product-photo" role="img" aria-label="Red and orange hypericum berries" style="background:radial-gradient(circle,#c8402e,#a83a22 40%,#d9902e 65%,#4e7a2a)"></div><div class="product-label">Hypericum Berry</div></div>
    <div class="product" style="left:424px"><div class="product-photo" role="img" aria-label="Crimson kangaroo paw flowers" style="background:radial-gradient(circle,#a82440,#8a1a30 60%,#c9d2c0)"></div><div class="product-label">Kangaroo Paws</div></div>
    <div class="product" style="left:614px"><div class="product-photo" role="img" aria-label="Orange Asiatic lily" style="background:radial-gradient(circle,#f6a020,#f5a83a 45%,#fbfbf8 75%)"></div><div class="product-label">Lilies Asiatic</div></div>
  </section>

  <section class="shelf" style="top:969px">
    <div class="shelf-board"></div>
    <div class="product" style="left:45px"><div class="product-photo" role="img" aria-label="Pink oriental lily" style="background:radial-gradient(circle,#c9407a,#e7a2c6 45%,#5a6a4a)"></div><div class="product-label">Lilies Oriental</div></div>
    <div class="product" style="left:235px"><div class="product-photo" role="img" aria-label="Lavender matthiola stock flowers" style="background:radial-gradient(circle,#d9cce4,#b8a6cc 60%,#7a6a8a)"></div><div class="product-label">Matthiola incana</div></div>
    <div class="product" style="left:424px"><div class="product-photo" role="img" aria-label="Bunch of mixed greens" style="background:radial-gradient(circle,#8cb454,#6e9a3a 60%,#f4f6ee 85%)"></div><div class="product-label">Mixed Greens</div></div>
    <div class="product" style="left:614px"><div class="product-photo" role="img" aria-label="Hot pink rose" style="background:radial-gradient(circle,#a80c44,#dc1a62 45%,#e0266e 80%)"></div><div class="product-label">Roses Hot Pink</div></div>
  </section>

  <footer class="site">www.brindlemeadowgoods.com</footer>
</body>
</html>
```